Brightpath Ventures

Marion T Haskell
"Title" Adventure Manager & Host
2871 North 42nd Street | Vancouver, BC | V5R 2B8
Direct 604.555. 0187 x 215
Skype drum41
1.800.555.0143
brightpathvx.ca
(perhaps small coastal tour bureau logo somewhere? Or “Powered by CTB”?)
- Grey/white logo cut out on reverse of card with web address

Industry/Entity Type

Travel

```html
<!DOCTYPE html>
<html lang="en">
<head>
<meta charset="utf-8">
<title>Brightpath Ventures – Card Reverse</title>
<link rel="stylesheet" href="https://fonts.googleapis.com/css2?family=Orbitron:wght@700&family=Questrial&display=swap">
<style>
  :root {
    --paper: #ffffff;
    --accent-green: #80e61c;
    --ink-grey: #3c3e41;
    --ink-dark: #2b2d30;
  }
  html, body {
    margin: 0;
    padding: 0;
    overflow: hidden;
    background: var(--paper);
  }
  .card-reverse {
    position: relative;
    width: 1200px;
    height: 702px;
    background: var(--paper);
    overflow: hidden;
  }
  .brand-lockup {
    position: absolute;
    left: 0;
    right: 0;
    top: 228px;
    height: 172px;
    display: flex;
    align-items: center;
    justify-content: center;
    gap: 34px;
  }
  .brand-square {
    width: 150px;
    height: 150px;
    background: var(--accent-green);
  }
  .brand-divider {
    width: 4px;
    height: 146px;
    background: var(--ink-grey);
  }
  .brand-name {
    margin: 0;
    font-family: "Orbitron", sans-serif;
    font-weight: 700;
    font-size: 50px;
    line-height: 1.25;
    letter-spacing: 2px;
    color: var(--ink-dark);
    text-transform: uppercase;
  }
  .brand-name span {
    display: block;
  }
  .web-address {
    position: absolute;
    left: 0;
    right: 0;
    top: 530px;
    margin: 0;
    text-align: center;
    font-family: "Questrial", sans-serif;
    font-size: 38px;
    color: var(--ink-grey);
  }
</style>
</head>
<body>
  <main class="card-reverse">
    <div class="brand-lockup">
      <div class="brand-square"></div>
      <div class="brand-divider"></div>
      <h1 class="brand-name"><span>Brightpath</span><span>Ventures</span></h1>
    </div>
    <p class="web-address">brightpathvx.ca</p>
  </main>
</body>
</html>
```